Business Broker Website

Hi.
I need a new design done for a business broker website. An example of the style of website I like is https://marlowpartners.example/
The menu needs to be :
* Home
* Businesses for Sale
* What we do
* Our people
* Industries
* Blog
* Confidentiality
* Contact
The home page needs to include a section saying 'businesses sold' with each having a photo, heading and short description. It also needs to have a place to show a video which I have attached so you can take a screenshot to put it on the page.
The content on the home page needs to be as follows:
Venture Transfer Partners are a boutique brokerage business, specializing in the sales and marketing of SME businesses throughout Queensland and, the Northern Territory
who we are
Welcome to Venture Transfer Partners. Our specialization is in the marketing and acquisition of closely held businesses throughout Queensland and the Northern Territory. We concentrate in SME businesses in the turnovers of approximately $1,000,000 to $10,000,000 +.
The combined business experience and industry knowledge of our principal is unparalleled and fully committed to a “customer first always” approach to doing business.
Our seller’s benefit from a multi-faceted strategic marketing plan, custom prepared for each seller, no two marketing campaigns are the same. This assures maximum exposure to well-qualified Buyers, while strictly maintaining confidentiality.
We have the comprehensive knowledge and resources to help our Buyers identify their perfect business acquisition– perhaps even if that business is not currently listed for sale!
"the whole secret of a successful life is to find out what is one's destiny to do, and then do it." walter pimm
Target Market(s)
people looking to buy or sell businesses
Number of Pages Required
1 page
Look and feel

```html
<!DOCTYPE html>
<html lang="en">
<head>
<meta charset="utf-8">
<title>Venture Transfer Partners – Business Brokers</title>
<link rel="stylesheet" href="https://fonts.googleapis.com/css2?family=Montserrat:wght@400;500;600;700&family=Lato:wght@400;700&family=Dancing+Script:wght@600&display=swap">
<style>
:root{
  --purple:#5b3f8e;
  --purple-dark:#3f2a6b;
  --purple-band:#6a4e9c;
  --orange:#f57c0b;
  --ink:#1e1e24;
  --text:#555a63;
  --muted:#8b8f97;
  --line:#e4e4ea;
  --footer:#17171d;
  --white:#ffffff;
}
*{box-sizing:border-box;margin:0;padding:0}
html,body{width:1200px;height:4887px;overflow:hidden}
body{font-family:"Lato",Arial,sans-serif;color:var(--text);background:var(--white);position:relative}
h1,h2,h3,h4,.btn,.nav a{font-family:"Montserrat",Arial,sans-serif}
.abs{position:absolute}
.btn{position:absolute;display:inline-flex;align-items:center;gap:10px;background:var(--orange);color:#fff;font-weight:600;font-size:15px;height:42px;padding:0 26px;border-radius:3px;text-decoration:none;box-shadow:0 4px 10px rgba(245,124,11,.25);white-space:nowrap}
.btn svg{width:16px;height:16px}
.section{position:absolute;left:0;width:1200px}

/* header */
.site-header{top:0;height:80px;background:#fff}
.brand{position:absolute;left:63px;top:27px;display:flex;align-items:center;gap:9px;font-family:"Montserrat",sans-serif;font-weight:700;font-size:14px;color:var(--purple);white-space:nowrap}
.brand .dot{width:26px;height:26px;border-radius:50%;background:var(--purple)}
.nav{position:absolute;left:341px;top:34px;width:670px;display:flex;justify-content:space-between}
.nav a{font-size:12px;color:#333;text-decoration:none;font-weight:500;white-space:nowrap}
.login{position:absolute;left:1058px;top:26px;display:flex;align-items:center;gap:10px;font-family:"Montserrat",sans-serif;font-size:13px;color:var(--purple);font-weight:600}
.login span.ic{width:30px;height:30px;border-radius:50%;background:var(--purple);display:flex;align-items:center;justify-content:center}

/* hero */
.hero{top:80px;height:508px;background:linear-gradient(180deg,#6b5a55 0%,#c98a52 35%,#8a6a5c 60%,#3f4a57 100%)}
.hero-shade{position:absolute;inset:0;background:rgba(20,20,30,.35)}
.hero h1{position:absolute;top:165px;left:0;width:1200px;text-align:center;color:#fff;font-size:39px;line-height:48px;font-weight:700;letter-spacing:.5px}
.hero p{position:absolute;top:270px;left:350px;width:500px;text-align:center;color:#f3eee9;font-size:13.5px;line-height:19px}
.hero .btn{left:499px;top:352px}

/* who we are */
.who{top:588px;height:588px}
.who-photo{position:absolute;left:60px;top:60px}
.section-title{display:flex;align-items:center;gap:16px;position:absolute}
.section-title .mark{width:52px;height:52px;border-radius:50%;background:var(--purple)}
.section-title h2{font-size:32px;font-weight:600;color:var(--ink);white-space:nowrap}
.body-copy{position:absolute;font-size:13.5px;line-height:22px;color:#3e4149}
.body-copy p+p{margin-top:14px}

/* trusted */
.trusted{top:1176px;height:512px;background:linear-gradient(90deg,#eceef2 0%,#f6f7f9 40%,#ffffff 55%)}
.trusted-photo{position:absolute;left:626px;top:0;width:569px;height:512px;background:linear-gradient(135deg,#dfe6ee 0%,#9fb4c9 40%,#2f3f5e 70%,#1c2840 100%)}
.quote-card{position:absolute;left:505px;top:404px;width:578px;height:146px;background:#fff;border-radius:6px;box-shadow:0 8px 24px rgba(0,0,0,.12);text-align:center}
.quote-card .qi{width:30px;height:30px;border-radius:50%;background:#fff2e6;color:var(--orange);margin:14px auto 6px;font-family:Georgia,serif;font-size:24px;line-height:34px}
.quote-card p{font-style:italic;font-size:15.5px;line-height:26px;color:#555;padding:0 60px}
.quote-card .sig{font-family:"Dancing Script",cursive;color:var(--purple);font-size:19px;margin-top:4px}

/* listings */
.discover{top:1688px;height:778px}
.center-title{position:absolute;left:0;width:1200px;text-align:center;font-size:38px;font-weight:500;color:var(--ink)}
.card{position:absolute;top:203px;width:300px;height:390px;background:#fff;box-shadow:0 4px 18px rgba(0,0,0,.1);border-radius:4px}
.card .ph{position:absolute;left:6px;top:6px;width:288px;height:200px;background:linear-gradient(180deg,#7fb2df 0%,#c9d6c6 45%,#4d7d3d 75%,#2f5a2a 100%)}
.card .badge{position:absolute;right:18px;top:18px;background:var(--orange);color:#fff;font-family:"Montserrat",sans-serif;font-weight:700;font-size:11px;padding:4px 10px;letter-spacing:1px;border-radius:2px}
.card h3{position:absolute;left:22px;top:225px;font-size:18px;font-weight:500;color:var(--ink)}
.card .heart{position:absolute;right:22px;top:228px}
.card .addr{position:absolute;left:22px;top:252px;font-size:9.5px;color:var(--muted)}
.stats{position:absolute;left:22px;top:286px;display:flex}
.stats div{padding-right:16px;margin-right:16px;border-right:1px solid var(--line)}
.stats div:last-child{border:none}
.stats b{display:block;font-size:13.5px;color:var(--ink);font-weight:700}
.stats span{font-size:9.5px;color:var(--muted)}
.card .agent{position:absolute;left:22px;top:350px;display:flex;align-items:center;gap:8px;font-size:10px;color:var(--muted)}
.card .agent i{width:26px;height:26px;border-radius:50%;background:#b7a495;display:block}
.card .price{position:absolute;right:22px;top:350px;font-family:"Montserrat",sans-serif;color:var(--orange);font-weight:700;font-size:19px}
.arrow-btn{position:absolute;top:2064px;width:30px;height:30px;border-radius:50%;display:flex;align-items:center;justify-content:center}

/* what we do */
.what{top:2466px;height:680px}
.what-band{position:absolute;left:0;top:0;width:1200px;height:380px;background:linear-gradient(180deg,var(--purple) 0%,var(--purple-band) 100%)}
.video{position:absolute;left:241px;top:148px;width:719px;height:402px;background:#fff;padding:9px;box-shadow:0 10px 30px rgba(0,0,0,.18)}
.video .frame{position:relative;width:100%;height:100%;background:linear-gradient(180deg,#e6e6e8 0%,#dcdcdf 70%,#c9c9cc 100%)}
.video .play{position:absolute;left:306px;top:130px;width:88px;height:88px;border-radius:50%;background:#fff;display:flex;align-items:center;justify-content:center;box-shadow:0 4px 14px rgba(0,0,0,.2)}
.video .caption{position:absolute;left:0;bottom:0;width:100%;height:52px;background:rgba(90,90,95,.55);color:#fff;text-align:center;font-size:15.5px;line-height:21px;padding-top:5px}

/* blog */
.blog{top:3146px;height:667px}
.post-lg{position:absolute;left:118px;top:60px;width:470px;height:455px;background:#fff;box-shadow:0 4px 18px rgba(0,0,0,.1)}
.post-lg .ph{position:absolute;left:7px;top:7px;width:456px;height:281px;background:linear-gradient(135deg,#e9ecef 0%,#b8bec6 45%,#8b7a6a 75%,#dadde1 100%)}
.meta{font-size:10.5px;color:var(--muted);white-space:nowrap}
.meta span{margin-left:16px}
.post-lg .meta{position:absolute;left:30px;top:306px}
.post-lg h3{position:absolute;left:30px;top:328px;width:425px;font-size:18.5px;line-height:28px;font-weight:500;color:var(--ink)}
.more{position:absolute;display:flex;align-items:center;gap:8px;font-family:"Montserrat",sans-serif;font-size:14px;font-weight:500;color:var(--orange);text-decoration:none}
.post-lg .more{left:30px;top:412px}
.post-sm{position:absolute;left:611px;width:472px;height:210px;background:#fff;box-shadow:0 4px 18px rgba(0,0,0,.1)}
.post-sm .ph{position:absolute;left:11px;top:9px;width:213px;height:196px;background:linear-gradient(180deg,#4f86c9 0%,#9bbbe0 45%,#596c7c 65%,#3d5d3a 100%)}
.post-sm .meta{position:absolute;left:250px;top:20px}
.post-sm h4{position:absolute;left:250px;top:38px;width:210px;font-size:13.5px;line-height:19px;font-weight:600;color:var(--ink)}
.post-sm p{position:absolute;left:250px;top:92px;width:205px;font-size:10px;line-height:16px;color:var(--muted)}
.post-sm .more{left:250px;top:172px;font-size:13px}

/* find form */
.find{top:3813px;height:575px;background:linear-gradient(180deg,#f1f1f3 0%,#fafafb 60%,#f4f4f6 100%)}
.find .mark{position:absolute;left:574px;top:38px;width:60px;height:60px;border-radius:50%;background:var(--purple)}
.find h2{position:absolute;left:0;top:114px;width:1200px;text-align:center;font-size:33px;line-height:43px;font-weight:500;color:var(--ink)}
.find .lead{position:absolute;left:370px;top:212px;width:460px;text-align:center;font-size:13px;line-height:19px;color:var(--muted)}
.field{position:absolute;background:#fff;border:1px solid var(--line);font-size:11px;color:#666;padding:12px 14px}
.field.active{border-color:var(--orange)}
.find .btn{left:525px;top:500px}

/* footer */
.site-footer{top:4388px;height:499px;background:var(--footer);color:#cfcfd4}
.sub-label{position:absolute;left:118px;top:64px;font-size:18px;color:#e6e6ea}
.site-footer h2{position:absolute;left:118px;top:92px;font-size:41px;font-weight:600;color:#fff;letter-spacing:.5px}
.subscribe{position:absolute;left:592px;top:93px;width:489px;height:38px;border:1px solid #55555c;border-radius:3px}
.subscribe span{position:absolute;left:16px;top:12px;font-size:11px;color:#8a8a92}
.subscribe b{position:absolute;right:3px;top:3px;height:30px;width:150px;background:var(--orange);color:#fff;border-radius:2px;font-family:"Montserrat",sans-serif;font-size:14px;font-weight:600;display:flex;align-items:center;justify-content:center}
.rule{position:absolute;left:118px;width:965px;height:1px;background:#3a3a42}
.f-brand{position:absolute;left:118px;top:224px;display:flex;align-items:center;gap:9px;font-family:"Montserrat",sans-serif;font-weight:700;font-size:13.5px;color:#fff;white-space:nowrap}
.f-brand .dot{width:26px;height:26px;border-radius:50%;background:#fff}
.f-about{position:absolute;left:118px;top:282px;width:240px;font-size:10px;line-height:15px;color:#bdbdc4}
.f-col{position:absolute;top:222px}
.f-col h4{font-size:11px;font-weight:700;color:#fff;letter-spacing:.5px;position:relative;padding-bottom:10px;margin-bottom:14px;white-space:nowrap}
.f-col h4:after{content:"";position:absolute;left:0;bottom:0;width:32px;height:2px;background:var(--orange)}
.f-col a{display:block;font-size:11.5px;color:#d1d1d6;text-decoration:none;margin-bottom:10px;white-space:nowrap}
.f-contact div{display:flex;gap:10px;font-size:11.5px;line-height:16px;color:#d1d1d6;margin-bottom:14px;white-space:nowrap}
.f-contact div.big{font-size:14px}
.social{position:absolute;left:524px;top:415px;display:flex;gap:14px}
.social i{width:26px;height:26px;border-radius:50%;background:var(--orange);display:block}
.copy{position:absolute;left:0;top:460px;width:1200px;text-align:center;font-size:10px;color:#9a9aa2}
</style>
</head>
<body>

<header class="section site-header">
  <div class="brand"><span class="dot"></span>Venture Transfer Partners</div>
  <nav class="nav">
    <a href="#">Home</a><a href="#">Businesses for Sale</a><a href="#">What we do</a><a href="#">Our people</a><a href="#">Industries</a><a href="#">Blog</a><a href="#">Confidentiality</a><a href="#">Contact</a>
  </nav>
  <div class="login"><span class="ic"><svg width="14" height="14" viewBox="0 0 14 14" fill="none" stroke="#fff" stroke-width="1.5"><circle cx="7" cy="4.5" r="2.5"/><path d="M2 13c0-3 2.2-4.5 5-4.5s5 1.5 5 4.5"/></svg></span>Login</div>
</header>

<section class="section hero">
  <div class="abs" style="inset:0" role="img" aria-label="City skyline and river bridge at sunset"></div>
  <div class="hero-shade"></div>
  <h1>A BUSINESS BROKER COMPANY<br>THAT IS FOCUSED ON YOU</h1>
  <p>Venture Transfer Partners are a boutique brokerage business, specializing in the sales and marketing of SME businesses throughout Queensland and, the Northern Territory</p>
  <a class="btn" href="#">Find Your Business</a>
</section>

<section class="section who">
  <svg class="who-photo" width="520" height="470" viewBox="0 0 520 470">
    <defs>
      <linearGradient id="meet" x1="0" y1="0" x2="1" y2="1">
        <stop offset="0" stop-color="#e8eaee"/><stop offset=".5" stop-color="#9aa1ab"/><stop offset="1" stop-color="#4b4f58"/>
      </linearGradient>
    </defs>
    <path d="M188 22 A226 226 0 1 1 188 446" fill="none" stroke="var(--purple)" stroke-width="12" stroke-linecap="round"/>
    <circle cx="258" cy="234" r="208" fill="url(#meet)" role="img" aria-label="Business meeting around a table"/>
  </svg>
  <div class="section-title" style="left:665px;top:136px"><span class="mark"></span><h2>Who We Are</h2></div>
  <div class="body-copy" style="left:670px;top:212px;width:405px">
    <p>Welcome to Venture Transfer Partners. Our specialization is in the marketing and acquisition of closely held businesses throughout Queensland and the Northern Territory. We concentrate in SME businesses in the turnovers of approximately $1,000,000 to $10,000,000 +.</p>
    <p>The combined business experience and industry knowledge of our principal is unparalleled and fully committed to a “customer first always” approach to doing business.</p>
  </div>
  <a class="btn" href="#" style="left:670px;top:431px">Learn More <svg viewBox="0 0 16 16" fill="none" stroke="#fff" stroke-width="2"><path d="M2 8h11M9 4l4 4-4 4"/></svg></a>
</section>

<section class="section trusted">
  <div class="trusted-photo" role="img" aria-label="Two businessmen shaking hands in an office"></div>
  <div class="section-title" style="left:113px;top:92px"><span class="mark"></span><h2>We Are Trusted</h2></div>
  <div class="body-copy" style="left:117px;top:175px;width:475px">
    <p>Our seller’s benefit from a multi-faceted strategic marketing plan, custom prepared for each seller, no two marketing campaigns are the same. This assures maximum exposure to well-qualified Buyers, while strictly maintaining confidentiality.</p>
    <p style="margin-top:20px">We have the comprehensive knowledge and resources to help our Buyers identify their perfect business acquisition– perhaps even if that business is not currently listed for sale!</p>
  </div>
  <a class="btn" href="#" style="left:117px;top:380px">Learn More <svg viewBox="0 0 16 16" fill="none" stroke="#fff" stroke-width="2"><path d="M2 8h11M9 4l4 4-4 4"/></svg></a>
  <div class="quote-card">
    <div class="qi">”</div>
    <p>The whole secret of a successful life is to find out what is one's destiny to do, and then do it</p>
    <div class="sig">Walter Pimm</div>
  </div>
</section>

<section class="section discover">
  <h2 class="center-title" style="top:108px">Discover New Businesses</h2>

  <article class="card" style="left:118px">
    <div class="ph" role="img" aria-label="Waterfront apartment towers with palm trees"></div>
    <h3>Bluewater Lagoon</h3>
    <svg class="heart" width="16" height="14" viewBox="0 0 16 14"><path d="M8 13.5S1 9 1 4.5A3.5 3.5 0 0 1 8 3a3.5 3.5 0 0 1 7 1.5C15 9 8 13.5 8 13.5z" fill="#c9c9cf"/></svg>
    <div class="addr">418 Harbour Rd. Cairns, QLD 4870</div>
    <div class="stats"><div><b>$150,000</b><span>Cash Flow</span></div><div><b>$1,500,000</b><span>Gross Revenue</span></div><div><b>N/a</b><span>EBITDA</span></div></div>
    <div class="agent"><i role="img" aria-label="Agent portrait"></i>Dana Keller, QLD</div>
    <div class="price">$150,000</div>
  </article>

  <article class="card" style="left:450px">
    <div class="ph" role="img" aria-label="Waterfront apartment towers with palm trees"></div>
    <span class="badge">NEW</span>
    <h3>Bluewater Lagoon</h3>
    <svg class="heart" width="16" height="14" viewBox="0 0 16 14"><path d="M8 13.5S1 9 1 4.5A3.5 3.5 0 0 1 8 3a3.5 3.5 0 0 1 7 1.5C15 9 8 13.5 8 13.5z" fill="#c9c9cf"/></svg>
    <div class="addr">418 Harbour Rd. Cairns, QLD 4870</div>
    <div class="stats"><div><b>$150,000</b><span>Cash Flow</span></div><div><b>$1,500,000</b><span>Gross Revenue</span></div><div><b>N/a</b><span>EBITDA</span></div></div>
    <div class="agent"><i role="img" aria-label="Agent portrait"></i>Dana Keller, QLD</div>
    <div class="price">$150,000</div>
  </article>

  <article class="card" style="left:780px">
    <div class="ph" role="img" aria-label="Waterfront apartment towers with palm trees"></div>
    <h3>Bluewater Lagoon</h3>
    <svg class="heart" width="16" height="14" viewBox="0 0 16 14"><path d="M8 13.5S1 9 1 4.5A3.5 3.5 0 0 1 8 3a3.5 3.5 0 0 1 7 1.5C15 9 8 13.5 8 13.5z" fill="#c9c9cf"/></svg>
    <div class="addr">418 Harbour Rd. Cairns, QLD 4870</div>
    <div class="stats"><div><b>$150,000</b><span>Cash Flow</span></div><div><b>$1,500,000</b><span>Gross Revenue</span></div><div><b>N/a</b><span>EBITDA</span></div></div>
    <div class="agent"><i role="img" aria-label="Agent portrait"></i>Dana Keller, QLD</div>
    <div class="price">$150,000</div>
  </article>

  <a class="btn" href="#" style="left:518px;top:654px">Find Out More</a>
</section>
<span class="arrow-btn" style="left:62px;border:1px solid #f0c9a3;background:#fff"><svg width="10" height="10" viewBox="0 0 10 10" fill="none" stroke="#f57c0b" stroke-width="1.6"><path d="M6.5 2L3.5 5l3 3"/></svg></span>
<span class="arrow-btn" style="left:1107px;background:var(--orange)"><svg width="10" height="10" viewBox="0 0 10 10" fill="none" stroke="#fff" stroke-width="1.6"><path d="M3.5 2l3 3-3 3"/></svg></span>

<section class="section what">
  <div class="what-band"></div>
  <h2 class="center-title" style="color:#fff;top:58px">What We Do</h2>
  <div class="video">
    <div class="frame" role="img" aria-label="Video still: animated businessman at a desk in an office">
      <span class="play"><svg width="40" height="40" viewBox="0 0 40 40"><circle cx="20" cy="20" r="20" fill="var(--orange)"/><path d="M16 12l12 8-12 8z" fill="#fff"/></svg></span>
      <div class="caption">If you are Private Business and you are thinking<br>of selling now or in the future</div>
    </div>
  </div>
</section>

<section class="section blog">
  <h2 class="center-title" style="font-size:32px;top:0">Our Latest Blog</h2>
  <article class="post-lg">
    <div class="ph" role="img" aria-label="Colleagues reviewing documents together"></div>
    <div class="meta">By Admin<span>January 10, 2022</span></div>
    <h3>Lorem ipsum dolor sit amet, consectetur laoreet parturient dui duis diam a, eget.</h3>
    <a class="more" href="#">Learn More <svg width="16" height="16" viewBox="0 0 16 16" fill="none" stroke="#f57c0b" stroke-width="2"><path d="M2 8h11M9 4l4 4-4 4"/></svg></a>
  </article>
  <article class="post-sm" style="top:60px">
    <div class="ph" role="img" aria-label="City skyline across a river"></div>
    <div class="meta">By Admin<span>January 10, 2022</span></div>
    <h4>Lorem ipsum dolor sit amet, consectetur laoreet.</h4>
    <p>Lorem ipsum dolor sit amet, consectetur adipiscing elit. Laoreet parturient dui duis diam a, eget. Orci imperdiet ac ac in curabitur...</p>
    <a class="more" href="#">Learn More <svg width="16" height="16" viewBox="0 0 16 16" fill="none" stroke="#f57c0b" stroke-width="2"><path d="M2 8h11M9 4l4 4-4 4"/></svg></a>
  </article>
  <article class="post-sm" style="top:291px">
    <div class="ph" role="img" aria-label="City skyline across a river"></div>
    <div class="meta">By Admin<span>January 10, 2022</span></div>
    <h4>Lorem ipsum dolor sit amet, consectetur laoreet.</h4>
    <p>Lorem ipsum dolor sit amet, consectetur adipiscing elit. Laoreet parturient dui duis diam a, eget. Orci imperdiet ac ac in curabitur...</p>
    <a class="more" href="#">Learn More <svg width="16" height="16" viewBox="0 0 16 16" fill="none" stroke="#f57c0b" stroke-width="2"><path d="M2 8h11M9 4l4 4-4 4"/></svg></a>
  </article>
  <a class="btn" href="#" style="left:518px;top:560px">View All Articles</a>
</section>

<section class="section find">
  <span class="mark"></span>
  <h2>We Will Find You The Perfect<br>Company To Buy</h2>
  <p class="lead">Lorem ipsum dolor sit amet, consectetur adipiscing elit. Laoreet parturient dui duis diam a, eget. Orci imperdiet ac ac in curabitur...</p>
  <div class="field active" style="left:281px;top:262px;width:313px;height:40px">First Name</div>
  <div class="field" style="left:605px;top:262px;width:313px;height:40px">Last Name</div>
  <div class="field" style="left:281px;top:315px;width:313px;height:40px">Your Phone</div>
  <div class="field" style="left:605px;top:315px;width:313px;height:40px">Email Address</div>
  <div class="field" style="left:281px;top:368px;width:637px;height:95px">Your Message Here..</div>
  <a class="btn" href="#">Submit Now</a>
</section>

<footer class="section site-footer">
  <div class="sub-label">Subscribe</div>
  <h2>GET IN TOUCH</h2>
  <div class="subscribe"><span>Enter email address</span><b>Submit Now</b></div>
  <div class="rule" style="top:165px"></div>

  <div class="f-brand"><span class="dot"></span>Venture Transfer Partners</div>
  <p class="f-about">We help owners sell and buyers acquire established SME businesses across Queensland and the Northern Territory with care and complete discretion.</p>

  <div class="f-col" style="left:398px"><h4>NAVIGATION</h4><a href="#">Home</a><a href="#">Businesses for Sale</a><a href="#">What we do</a><a href="#">Our people</a></div>
  <div class="f-col" style="left:582px"><h4>USEFULL LINKS</h4><a href="#">Industries</a><a href="#">Blog</a><a href="#">Confidentiality</a><a href="#">Contact</a></div>
  <div class="f-col" style="left:745px"><h4>ACCOUNT</h4><a href="#">Sign Up</a><a href="#">Login</a><a href="#">Account Setting</a></div>
  <div class="f-col f-contact" style="left:910px"><h4>CONTACT</h4>
    <div><svg width="14" height="16" viewBox="0 0 14 16" fill="none" stroke="#f57c0b" stroke-width="1.5"><path d="M7 15s5-5 5-9a5 5 0 0 0-10 0c0 4 5 9 5 9z"/><circle cx="7" cy="6" r="1.8"/></svg><span>88 Ridgeline St.<br>Darwin, NT 0800</span></div>
    <div class="big"><svg width="16" height="16" viewBox="0 0 16 16" fill="none" stroke="#f57c0b" stroke-width="1.5"><path d="M3 1.5l3 .5 1 3-2 1.5a9 9 0 0 0 4.5 4.5L11 9l3 1 .5 3-2 1.5C7 14 2 9 1.5 3.5z"/></svg>(07) 5550 1234</div>
    <div><svg width="16" height="14" viewBox="0 0 16 14" fill="none" stroke="#f57c0b" stroke-width="1.5"><rect x="1" y="1.5" width="14" height="11" rx="1"/><path d="M1 2l7 6 7-6"/></svg>hello@venturetransfer.example</div>
  </div>

  <div class="rule" style="top:428px;width:390px"></div>
  <div class="rule" style="top:428px;left:693px;width:390px"></div>
  <div class="social"><i></i><i></i><i></i><i></i></div>
  <div class="copy">©Copyright 2021. Venture Transfer Partners | All Rights Reserved</div>
</footer>

</body>
</html>
```